Pediatric Dental Practice needs a postcard for direct mail advertising

We are looking for a creative and professional double-sided postcard design for a direct mail marketing campaign. Our goal is to attract new families to our pediatric dental practice by conveying a sense of warmth, modern care, and clinical excellence. The design should feel "boutique" and high-end yet remain fun and approachable for parents and children.

```html
<!DOCTYPE html>
<html lang="en">
<head>
<meta charset="utf-8">
<title>Aspen Grove Pediatric Dentistry – Postcard</title>
<link href="https://fonts.googleapis.com/css2?family=Montserrat:wght@400;500;600;700;800;900&display=swap" rel="stylesheet">
<style>
  :root{
    --cream:#f3efdc;
    --green:#3a9b5c;
    --green-text:#2f9a55;
    --mint:#b4ddb6;
    --mint-icon:#a9d9ad;
    --charcoal:#3a3a3c;
    --ink:#2b2b2b;
    --white:#ffffff;
    --paper:#f3f3f3;
    --rule:#c9c9c9;
    --stage:#e4e4e4;
  }
  *{margin:0;padding:0;box-sizing:border-box}
  html,body{width:1200px;height:900px;overflow:hidden}
  body{background:var(--stage);font-family:"Montserrat",sans-serif;color:var(--ink);position:relative}

  .postcard{position:absolute;left:300px;width:600px;height:400px;overflow:hidden;box-shadow:0 4px 14px rgba(0,0,0,.18)}
  .postcard--front{top:35px;background:var(--cream)}
  .postcard--back{top:465px;background:var(--paper)}
  .shapes{position:absolute;inset:0;width:600px;height:400px}
  .layer{position:absolute}

  /* brand name block */
  .brand__name{font-weight:600;font-size:30px;color:var(--green);line-height:1;letter-spacing:.5px;display:flex;align-items:center;gap:8px}
  .brand__dot{width:16px;height:16px;border-radius:50%;background:var(--green);flex:none}
  .brand__sub{font-size:8px;letter-spacing:3.2px;color:var(--green);font-weight:500;margin-top:4px;padding-left:24px}

  /* front */
  .front-brand{left:38px;top:120px}
  .headline{left:22px;top:182px;color:var(--white);font-weight:900;font-size:25px;line-height:1.02;letter-spacing:.3px;text-transform:uppercase}
  .welcome{left:22px;top:240px;width:290px}
  .welcome__title{font-weight:800;font-size:10.5px;line-height:1.15;text-transform:uppercase;color:var(--ink)}
  .welcome__copy{margin-top:4px;font-size:7.4px;line-height:1.38;text-align:justify;color:var(--ink)}

  .contact{color:var(--white);font-weight:500;display:flex;align-items:center;gap:6px;font-size:11px;line-height:1.15}
  .icon{width:14px;height:14px;border-radius:50%;background:var(--mint-icon);display:inline-flex;align-items:center;justify-content:center;flex:none}
  .icon svg{width:9px;height:9px}
  .social{display:flex;gap:6px}
  .social__dot{width:14px;height:14px;border-radius:50%;background:var(--mint-icon)}

  .front-address{left:22px;top:344px}
  .front-phone{left:22px;top:377px}
  .front-email{left:232px;top:358px}
  .front-social{left:400px;top:330px}
  .front-web{left:390px;top:292px}

  /* back */
  .services{left:20px;top:22px}
  .services__title{font-weight:900;font-size:12.5px;text-transform:uppercase;color:var(--ink)}
  .services__cols{display:flex;gap:26px;margin-top:5px}
  .services__list{list-style:none}
  .services__list li{display:flex;align-items:center;gap:4px;font-size:7.6px;font-weight:600;line-height:1.55;color:var(--ink)}
  .tick{width:8px;height:8px;border-radius:50%;background:var(--green);display:inline-flex;align-items:center;justify-content:center;flex:none}
  .tick svg{width:6px;height:6px}

  .meet{left:20px;top:273px;width:350px}
  .meet__kicker{font-weight:800;font-size:9.5px;text-transform:uppercase;color:var(--ink)}
  .meet__name{font-weight:900;font-size:13px;text-transform:uppercase;color:var(--green-text);line-height:1.1}
  .meet__copy{margin-top:3px;font-size:7.2px;line-height:1.35;color:var(--ink)}

  .back-phone{left:20px;top:362px}
  .back-web{left:20px;top:381px}
  .back-social{left:330px;top:362px}

  .stamp{left:495px;top:20px;width:72px;height:56px;border:1.5px solid var(--rule)}
  .return{left:352px;top:84px}
  .return .brand__name{font-size:22px}
  .return .brand__dot{width:12px;height:12px}
  .return .brand__sub{font-size:6.5px;letter-spacing:2.6px;padding-left:20px}
  .return__address{margin-top:4px;padding-left:20px;font-size:7.5px;font-weight:700;line-height:1.3;color:var(--ink)}
  .mail-line{left:420px;width:160px;height:1.5px;background:var(--rule)}
</style>
</head>
<body>

<!-- FRONT -->
<section class="postcard postcard--front" aria-label="Postcard front">
  <svg class="shapes" viewBox="0 0 600 400">
    <path d="M0,168 H215 L240,218 L232,232 H0 Z" fill="var(--green)"/>
    <path d="M0,336 H290 C370,336 410,306 460,292 C515,276 560,272 600,256 V400 H0 Z" fill="var(--charcoal)"/>
    <path d="M300,58 C332,18 420,40 472,30 C542,16 592,30 586,102 C580,172 570,232 520,272 C470,308 360,302 300,296 C236,290 244,222 258,170 C272,120 268,100 300,58 Z" fill="var(--cream)" stroke="var(--cream)" stroke-width="6"/>
    <g role="img" aria-label="Photo of a pediatric dentist treating a young girl in the chair while a smiling mother holds her toddler">
      <defs>
        <linearGradient id="frontPhoto" x1="0" y1="0" x2="1" y2="1">
          <stop offset="0" stop-color="#e4d8c4"/>
          <stop offset=".45" stop-color="#5aa6a0"/>
          <stop offset="1" stop-color="#c9a77e"/>
        </linearGradient>
      </defs>
      <path d="M300,58 C332,18 420,40 472,30 C542,16 592,30 586,102 C580,172 570,232 520,272 C470,308 360,302 300,296 C236,290 244,222 258,170 C272,120 268,100 300,58 Z" fill="url(#frontPhoto)"/>
    </g>
  </svg>

  <div class="layer front-brand">
    <div class="brand__name"><span class="brand__dot"></span>aspen grove</div>
    <div class="brand__sub">PEDIATRIC DENTISTRY</div>
  </div>

  <h1 class="layer headline">Let your<br>smile grow!</h1>

  <div class="layer welcome">
    <h2 class="welcome__title">Welcome to Aspen Grove<br>Pediatric Dentistry</h2>
    <p class="welcome__copy">We understand that visiting the dentist can create anxiety and fear for young children. That's why we're committed to creating a fun and gentle dental experience for kids in Fairbrook, CT. Our pediatric dental team specializes in providing high-quality, compassionate care in a safe &amp; comfortable environment. We're dedicated to helping your child develop healthy oral habits for a lifetime of beautiful smiles!</p>
  </div>

  <div class="layer contact front-address">
    <span class="icon"><svg viewBox="0 0 10 10"><path d="M5,1 C3.2,1 2,2.3 2,4 C2,6 5,9 5,9 C5,9 8,6 8,4 C8,2.3 6.8,1 5,1 Z" fill="var(--charcoal)"/><circle cx="5" cy="4" r="1.1" fill="var(--mint-icon)"/></svg></span>
    <span>48 Meadow Lane,<br>Suite 210 Fairbrook, CT 06020</span>
  </div>
  <div class="layer contact front-phone">
    <span class="icon"><svg viewBox="0 0 10 10"><path d="M2.2,1.5 L3.6,1.5 L4.2,3.3 L3.3,4 C3.8,5.1 4.9,6.2 6,6.7 L6.7,5.8 L8.5,6.4 L8.5,7.8 C8.5,8.3 8.1,8.6 7.6,8.5 C4.6,8.1 1.9,5.4 1.5,2.4 C1.4,1.9 1.7,1.5 2.2,1.5 Z" fill="var(--charcoal)"/></svg></span>
    <span>(555) 014-2760</span>
  </div>
  <div class="layer contact front-email">
    <span class="icon"><svg viewBox="0 0 10 10"><rect x="1.5" y="2.8" width="7" height="4.6" rx=".6" fill="var(--charcoal)"/><path d="M1.8,3.1 L5,5.5 L8.2,3.1" stroke="var(--mint-icon)" stroke-width=".7" fill="none"/></svg></span>
    <span>hello@aspengrovedental.com</span>
  </div>
  <div class="layer social front-social" aria-label="Social media">
    <span class="social__dot"></span><span class="social__dot"></span>
  </div>
  <div class="layer contact front-web">
    <span class="icon"><svg viewBox="0 0 10 10"><circle cx="5" cy="5" r="3.4" fill="none" stroke="var(--charcoal)" stroke-width=".9"/><ellipse cx="5" cy="5" rx="1.4" ry="3.4" fill="none" stroke="var(--charcoal)" stroke-width=".8"/><path d="M1.6,5 H8.4" stroke="var(--charcoal)" stroke-width=".8"/></svg></span>
    <span>www.aspengrovedental.com</span>
  </div>
</section>

<!-- BACK -->
<section class="postcard postcard--back" aria-label="Postcard back">
  <svg class="shapes" viewBox="0 0 600 400">
    <defs>
      <linearGradient id="roomPhoto" x1="0" y1="0" x2="1" y2="1">
        <stop offset="0" stop-color="#e8dccb"/>
        <stop offset=".5" stop-color="#6fb3b0"/>
        <stop offset="1" stop-color="#d59a5a"/>
      </linearGradient>
      <linearGradient id="dentistPhoto" x1="0" y1="0" x2="0" y2="1">
        <stop offset="0" stop-color="#f2f2f2"/>
        <stop offset="1" stop-color="#a9c3dc"/>
      </linearGradient>
    </defs>
    <path d="M0,0 H320 C378,40 404,130 396,230 L396,262 H0 Z" fill="var(--mint)"/>
    <rect x="0" y="262" width="392" height="138" fill="var(--cream)"/>
    <g role="img" aria-label="Photo of a bright treatment room with a teal dental chair, small chairs and a window">
      <path d="M0,100 H390 C394,150 396,200 392,262 H0 Z" fill="url(#roomPhoto)"/>
    </g>
    <path d="M0,354 H370 L392,340 V400 H0 Z" fill="var(--charcoal)"/>
    <g role="img" aria-label="Portrait photo of the pediatric dentist in a light blue shirt with arms crossed">
      <rect x="376" y="196" width="96" height="148" fill="url(#dentistPhoto)"/>
    </g>
  </svg>

  <div class="layer services">
    <h2 class="services__title">Our Featured Services</h2>
    <div class="services__cols">
      <ul class="services__list">
        <li><span class="tick"><svg viewBox="0 0 6 6"><path d="M1.2,3.1 L2.5,4.3 L4.8,1.8" stroke="#fff" stroke-width=".9" fill="none"/></svg></span>Pediatric Preventive Dentistry</li>
        <li><span class="tick"><svg viewBox="0 0 6 6"><path d="M1.2,3.1 L2.5,4.3 L4.8,1.8" stroke="#fff" stroke-width=".9" fill="none"/></svg></span>Pediatric Restorative Dentistry</li>
        <li><span class="tick"><svg viewBox="0 0 6 6"><path d="M1.2,3.1 L2.5,4.3 L4.8,1.8" stroke="#fff" stroke-width=".9" fill="none"/></svg></span>Silver Diamine Fluoride</li>
        <li><span class="tick"><svg viewBox="0 0 6 6"><path d="M1.2,3.1 L2.5,4.3 L4.8,1.8" stroke="#fff" stroke-width=".9" fill="none"/></svg></span>Pediatric Emergencies</li>
      </ul>
      <ul class="services__list">
        <li><span class="tick"><svg viewBox="0 0 6 6"><path d="M1.2,3.1 L2.5,4.3 L4.8,1.8" stroke="#fff" stroke-width=".9" fill="none"/></svg></span>Pediatric Sedation</li>
        <li><span class="tick"><svg viewBox="0 0 6 6"><path d="M1.2,3.1 L2.5,4.3 L4.8,1.8" stroke="#fff" stroke-width=".9" fill="none"/></svg></span>Pediatric Dental Fillings</li>
        <li><span class="tick"><svg viewBox="0 0 6 6"><path d="M1.2,3.1 L2.5,4.3 L4.8,1.8" stroke="#fff" stroke-width=".9" fill="none"/></svg></span>Pediatric Dental Crowns</li>
        <li><span class="tick"><svg viewBox="0 0 6 6"><path d="M1.2,3.1 L2.5,4.3 L4.8,1.8" stroke="#fff" stroke-width=".9" fill="none"/></svg></span>Pediatric Pulpotomies</li>
      </ul>
    </div>
  </div>

  <div class="layer meet">
    <h2 class="meet__kicker">Meet your pediatric dentist</h2>
    <p class="meet__name">Dr. Owen Whitfield</p>
    <p class="meet__copy">Throughout his own childhood and during his academic and professional career in becoming a pediatric dentist, Dr. Whitfield has maintained a passion for connecting with others &amp; helping to make a difference in their lives. He is committed to making sure you and your child have a positive and enjoyable experience!</p>
  </div>

  <div class="layer contact back-phone">
    <span class="icon"><svg viewBox="0 0 10 10"><path d="M2.2,1.5 L3.6,1.5 L4.2,3.3 L3.3,4 C3.8,5.1 4.9,6.2 6,6.7 L6.7,5.8 L8.5,6.4 L8.5,7.8 C8.5,8.3 8.1,8.6 7.6,8.5 C4.6,8.1 1.9,5.4 1.5,2.4 C1.4,1.9 1.7,1.5 2.2,1.5 Z" fill="var(--charcoal)"/></svg></span>
    <span>(555) 014-2760</span>
  </div>
  <div class="layer contact back-web">
    <span class="icon"><svg viewBox="0 0 10 10"><circle cx="5" cy="5" r="3.4" fill="none" stroke="var(--charcoal)" stroke-width=".9"/><ellipse cx="5" cy="5" rx="1.4" ry="3.4" fill="none" stroke="var(--charcoal)" stroke-width=".8"/><path d="M1.6,5 H8.4" stroke="var(--charcoal)" stroke-width=".8"/></svg></span>
    <span>www.aspengrovedental.com</span>
  </div>
  <div class="layer social back-social" aria-label="Social media">
    <span class="social__dot"></span><span class="social__dot"></span>
  </div>

  <div class="layer stamp" aria-label="Stamp area"></div>
  <div class="layer return">
    <div class="brand__name"><span class="brand__dot"></span>aspen grove</div>
    <div class="brand__sub">PEDIATRIC DENTISTRY</div>
    <p class="return__address">48 Meadow Lane, Suite 210<br>Fairbrook, CT 06020</p>
  </div>
  <div class="layer mail-line" style="top:170px"></div>
  <div class="layer mail-line" style="top:200px"></div>
  <div class="layer mail-line" style="top:230px"></div>
</section>

</body>
</html>
```